Waschkarten-Design für Tankstelle gesucht
Zielgruppe
Unsere Tankstelle hat in eine neue Waschanlage investiert. Die Alten Waschkarten gefallen nicht mehr, und sind auch mit der Programmstruktur nicht mehr kompatibel. Siehe Anhang.
Waschkunden in der Portalwaschanlage jeglichen Alters und Geschlechts.
Aufgabenstellung
Wertigkeit der einzelnen Waschprogramme muss erkennbar sein. Beschriftung z. B. Mehrfachwäschen 3er 5er 10er bzw. Wertkarten der Preis soll veränderbar sein, so das die Karten jederzeit angepasst werden können. Auch sollte der Programm-Name von uns selbst geändert werden können. Die Einschiebe Richtung muss klar erkennbar sein.
Das Design muss im Check-Kartenformat sein. Achtung abgerundete Ecken mit ca. r=2 mm
Anbei ein Bild von unserer Neuen Waschanlage

```html
<!DOCTYPE html>
<html lang="de">
<head>
<meta charset="utf-8">
<title>Waschkarte Premium</title>
<link rel="stylesheet" href="https://fonts.googleapis.com/css2?family=Ubuntu:wght@400;700&display=swap">
<style>
  :root {
    --panel-top: #f7c81c;
    --panel-bottom: #d8a40c;
    --scene-light: #c9bd78;
    --scene-mid: #a39447;
    --scene-dark: #6f6530;
    --ground: #8d8346;
    --white: #ffffff;
    --shadow: #1c1a12;
    --ink: #1a1712;
    --arrow: rgba(255, 255, 255, 0.72);
  }
  html, body {
    margin: 0;
    padding: 0;
    width: 1200px;
    height: 757px;
    overflow: hidden;
    background: #ffffff;
  }
  .card {
    position: relative;
    width: 1200px;
    height: 757px;
    overflow: hidden;
    font-family: "Ubuntu", sans-serif;
  }
  .car-wash-scene {
    position: absolute;
    left: 413px;
    top: 0;
    width: 787px;
    height: 757px;
    background:
      linear-gradient(180deg, rgba(0,0,0,0) 0%, rgba(0,0,0,0) 72%, var(--ground) 72%, #a69c5c 100%),
      radial-gradient(ellipse at 50% 45%, var(--scene-dark) 0%, var(--scene-mid) 45%, var(--scene-light) 100%);
  }
  .brand-panel {
    position: absolute;
    left: 0;
    top: 0;
    width: 413px;
    height: 757px;
    background: linear-gradient(180deg, var(--panel-top) 0%, var(--panel-bottom) 100%);
  }
  .program-title {
    position: absolute;
    left: 40px;
    top: 38px;
    margin: 0;
    font-size: 164px;
    font-weight: 700;
    line-height: 1;
    color: var(--white);
    text-shadow: 5px 5px 0 var(--shadow);
    letter-spacing: 0;
  }
  .program-subtitle {
    position: absolute;
    left: 42px;
    top: 222px;
    margin: 0;
    font-size: 62px;
    font-weight: 400;
    line-height: 78px;
    color: var(--white);
    text-shadow: 3px 3px 0 var(--shadow);
  }
  .insert-arrow {
    position: absolute;
    left: 0;
    top: 0;
  }
  .price {
    position: absolute;
    left: 659px;
    top: 468px;
    margin: 0;
    font-size: 118px;
    font-weight: 700;
    line-height: 1;
    color: var(--white);
    text-shadow: 5px 5px 0 var(--shadow);
  }
  .station-name {
    position: absolute;
    left: 44px;
    top: 560px;
    margin: 0;
    font-size: 48px;
    font-weight: 700;
    line-height: 58px;
    color: var(--ink);
  }
</style>
</head>
<body>
  <main class="card">
    <div class="car-wash-scene" role="img" aria-label="Foto der neuen Portalwaschanlage mit Bürsten unter bewölktem Himmel, gelb getönt"></div>
    <div class="brand-panel"></div>

    <h1 class="program-title">PREMIUM</h1>
    <p class="program-subtitle">Politurprogramm mit<br>Unterbodenwäsche</p>

    <svg class="insert-arrow" width="1200" height="757" viewBox="0 0 1200 757" aria-hidden="true">
      <polygon points="600,487 896,487 896,410 1163,567 896,724 896,641 600,641" fill="var(--arrow)"/>
    </svg>
    <p class="price">€ 16,95</p>

    <p class="station-name">Tankstelle<br>Falkner</p>
  </main>
</body>
</html>
```